依頼詳細
当社のリーフレットやウェブサイトやその他資料に基づいたデザインでお願い致します。
記載項目
榊原会館 月照苑 有限会社みのり堂
https://gessho-en.example/
サイズ
A4
ページ数
4ページ
希望イメージ
シンプル 複雑
単色 カラフル
暗い 明るい
日常 高級
遊び心 厳粛
未来的 伝統的
女性的 男性的
希望する色
青系、水色系、無彩色系
納品ファイル
補足説明
■ 選んだ理由

この度の提案では従業員一同ぼんやりとイメージがありそれに一番近かった、またごちゃごちゃしていないデザイン、お花のチョイスなども決め手でした。

■ 提案者全員のお礼・コメント

はじめての依頼になりましたが、少量のページ数ながらみなさんのご提案はすばらしかったです。
資料を具体的にわかりやすくご提案いただいたのに採用できないことは非常に残念に感じます。
この度は誠にありがとうございました。

```html
<!DOCTYPE html>
<html lang="ja">
<head>
<meta charset="utf-8">
<title>月照苑 ご葬儀プランのご案内</title>
<link rel="stylesheet" href="https://fonts.googleapis.com/css2?family=Yuji+Syuku&family=Zen+Old+Mincho:wght@500;700&display=swap">
<style>
  :root {
    --paper: #ffffff;
    --ink: #2b2b2b;
    --ink-soft: #4a4a4a;
    --moon-tone: #c9cbcf;
    --wave: #e3e6eb;
    --cloud: #eceef1;
  }
  html, body {
    margin: 0;
    padding: 0;
    overflow: hidden;
    background: var(--paper);
  }
  .cover {
    position: relative;
    width: 849px;
    height: 1200px;
    overflow: hidden;
    background: var(--paper);
    font-family: "Zen Old Mincho", serif;
    color: var(--ink);
  }
  .backdrop {
    position: absolute;
    inset: 0;
  }
  .venue {
    position: absolute;
    left: 419px;
    top: 212px;
    transform: translateX(-50%);
    writing-mode: vertical-rl;
    margin: 0;
    font-size: 32px;
    font-weight: 500;
    line-height: 1;
    letter-spacing: 7px;
    color: var(--ink-soft);
  }
  .brand {
    position: absolute;
    left: 419px;
    top: 450px;
    transform: translateX(-50%);
    writing-mode: vertical-rl;
    margin: 0;
    font-family: "Yuji Syuku", serif;
    font-weight: 400;
    font-size: 112px;
    line-height: 1;
    letter-spacing: 16px;
    color: var(--ink);
  }
  .brand-reading {
    position: absolute;
    left: 498px;
    top: 495px;
    transform: translateX(-50%);
    writing-mode: vertical-rl;
    font-size: 13px;
    line-height: 1;
    letter-spacing: 34px;
    color: var(--ink-soft);
  }
  .subtitle {
    position: absolute;
    left: 0;
    right: 0;
    top: 982px;
    text-align: center;
    margin: 0;
    font-size: 29px;
    font-weight: 500;
    letter-spacing: 5px;
    color: var(--ink);
  }
  .company {
    position: absolute;
    left: 0;
    right: 0;
    top: 1132px;
    text-align: center;
    margin: 0;
    font-size: 20px;
    font-weight: 700;
    letter-spacing: 6px;
    color: var(--ink);
  }
</style>
</head>
<body>
<main class="cover">
  <svg class="backdrop" width="849" height="1200" viewBox="0 0 849 1200" xmlns="http://www.w3.org/2000/svg">
    <defs>
      <linearGradient id="wave-fade" x1="0" y1="0" x2="0" y2="1">
        <stop offset="0" stop-color="var(--wave)" stop-opacity="0"/>
        <stop offset="0.4" stop-color="var(--wave)" stop-opacity="0.8"/>
        <stop offset="0.85" stop-color="var(--wave)" stop-opacity="0.6"/>
        <stop offset="1" stop-color="var(--wave)" stop-opacity="0"/>
      </linearGradient>
      <radialGradient id="moon-fade" cx="0.5" cy="0.5" r="0.5">
        <stop offset="0" stop-color="var(--moon-tone)" stop-opacity="0"/>
        <stop offset="0.7" stop-color="var(--moon-tone)" stop-opacity="0.12"/>
        <stop offset="0.92" stop-color="var(--moon-tone)" stop-opacity="0.4"/>
        <stop offset="1" stop-color="var(--moon-tone)" stop-opacity="0"/>
      </radialGradient>
      <linearGradient id="cloud-fade-left" x1="0" y1="0" x2="1" y2="0">
        <stop offset="0" stop-color="var(--cloud)" stop-opacity="0.9"/>
        <stop offset="1" stop-color="var(--cloud)" stop-opacity="0"/>
      </linearGradient>
      <linearGradient id="cloud-fade-right" x1="1" y1="0" x2="0" y2="0">
        <stop offset="0" stop-color="var(--cloud)" stop-opacity="0.9"/>
        <stop offset="1" stop-color="var(--cloud)" stop-opacity="0"/>
      </linearGradient>
    </defs>

    <rect class="wave-area" role="img" aria-label="淡い灰色の青海波模様" x="0" y="425" width="849" height="650" fill="url(#wave-fade)"/>
    <rect class="moon-area" role="img" aria-label="灰色のぼかしの三日月の装飾" x="156" y="284" width="650" height="650" fill="url(#moon-fade)"/>
    <rect class="cloud-area-top" role="img" aria-label="淡い灰色の雲の装飾" x="0" y="55" width="370" height="160" fill="url(#cloud-fade-left)"/>
    <rect class="cloud-area-bottom" role="img" aria-label="淡い灰色の雲の装飾" x="560" y="900" width="289" height="170" fill="url(#cloud-fade-right)"/>
  </svg>

  <p class="venue">榊原会館</p>
  <h1 class="brand">月照苑</h1>
  <span class="brand-reading">げっしょうえん</span>
  <p class="subtitle">ご葬儀プランのご案内</p>
  <p class="company">有限会社みのり堂</p>
</main>
</body>
</html>
```